Consulting firm needs a professional letterhead design

We need a professional letterhead design which is simple but unique. It should carry attributes of the latest designs in the market suitable for professional environmental consultancies.

- The logo is attached for you to USE.
- Our preferred color scheme is that shown in the logo.
- Letterhead text color is your choice to make.
- Logo to the left and text to the right plus slogan/tagline is desirable for this letterhead.

Use any address etc. of your choice in the letterhead.

Target Market(s)

Consulting firms and government agencies

Industry/Entity Type

Environmental Consultant

Colors
acd037
fece3e
85cae6
3277b5

Requirements
Must have
• Logo supplied and color scheme must be used.
Nice to have
• Nexa font is used in the Logo, so it would ne nice to have nexa font in the letterhead too.

```html
<!DOCTYPE html>
<html lang="en">
<head>
<meta charset="utf-8">
<title>Verdanta Letterhead</title>
<link rel="stylesheet" href="https://fonts.googleapis.com/css2?family=Montserrat:wght@500;600&family=Noto+Sans:wght@400;600&display=swap">
<style>
  :root {
    --bg: #c4c4c4;
    --paper: #ffffff;
    --ink: #2f3553;
    --yellow: #f6c90f;
    --green: #6ab344;
    --teal-dark: #0d7fa2;
    --teal-light: #55c4d8;
    --orange: #f39a1f;
    --globe: #3a8fbf;
  }
  html, body {
    margin: 0;
    width: 1200px;
    height: 1200px;
    overflow: hidden;
    background: var(--bg);
  }
  .letterhead {
    position: absolute;
    left: 151px;
    top: 30px;
    width: 897px;
    height: 1140px;
    background: var(--paper);
    overflow: hidden;
  }
  .brand {
    position: absolute;
    left: 58px;
    top: 130px;
  }
  .brand-name {
    display: flex;
    align-items: center;
    gap: 10px;
    font-family: "Noto Sans", sans-serif;
    font-weight: 600;
    font-size: 29px;
    letter-spacing: 2px;
    color: var(--ink);
    line-height: 1;
  }
  .brand-dot {
    width: 18px;
    height: 18px;
    border-radius: 50%;
    background: var(--green);
  }
  .tagline {
    margin-top: 5px;
    font-family: "Montserrat", sans-serif;
    font-weight: 500;
    font-size: 12px;
    color: var(--ink);
  }
  .contact {
    position: absolute;
    left: 669px;
    top: 50px;
    font-family: "Noto Sans", sans-serif;
    font-style: normal;
    font-size: 12.5px;
    color: var(--ink);
    line-height: 16px;
  }
  .contact p { margin: 0; }
  .contact-lines { margin-top: 9px; }
  .contact-line {
    display: flex;
    align-items: center;
    gap: 4px;
    height: 17.5px;
  }
  .contact-line svg { width: 11px; height: 11px; flex: none; }
  .footer-band {
    position: absolute;
    left: 0;
    bottom: 0;
    width: 897px;
    height: 80px;
    display: block;
  }
</style>
</head>
<body>
  <div class="letterhead">
    <header class="brand">
      <div class="brand-name"><span class="brand-dot"></span>VERDANTA</div>
      <div class="tagline">Evidence for sound climate choices</div>
    </header>

    <address class="contact">
      <p>2480 Harbour Road, Suite 310</p>
      <p>Lakeview, ON, K7R 4M2</p>
      <div class="contact-lines">
        <div class="contact-line">
          <svg viewBox="0 0 12 12" aria-hidden="true"><path d="M2.5 1 L4.5 1 L5.3 3.6 L4 4.6 C4.6 6 5.9 7.4 7.4 8 L8.4 6.7 L11 7.5 L11 9.5 C11 10.3 10.3 11 9.5 11 C5 10.6 1.4 7 1 2.5 C1 1.7 1.7 1 2.5 1 Z" fill="var(--orange)"/></svg>
          555-214-3380
        </div>
        <div class="contact-line">
          <svg viewBox="0 0 12 12" aria-hidden="true"><rect x="3" y="1" width="6" height="3" fill="var(--green)"/><rect x="1" y="4.5" width="10" height="4.5" rx="1" fill="var(--green)"/><rect x="3" y="7.5" width="6" height="3.5" fill="#fff" stroke="var(--green)" stroke-width="1"/></svg>
          555-214-3391
        </div>
        <div class="contact-line">
          <svg viewBox="0 0 12 12" aria-hidden="true"><circle cx="6" cy="6" r="5" fill="none" stroke="var(--globe)" stroke-width="1.1"/><ellipse cx="6" cy="6" rx="2.2" ry="5" fill="none" stroke="var(--globe)" stroke-width="1"/><line x1="1" y1="6" x2="11" y2="6" stroke="var(--globe)" stroke-width="1"/></svg>
          www.verdanta-consult.com
        </div>
      </div>
    </address>

    <svg class="footer-band" viewBox="0 0 897 80" preserveAspectRatio="none" aria-hidden="true">
      <defs>
        <linearGradient id="bandGradient" x1="0" y1="0" x2="1" y2="0">
          <stop offset="0" stop-color="var(--teal-dark)"/>
          <stop offset="1" stop-color="var(--teal-light)"/>
        </linearGradient>
      </defs>
      <rect x="0" y="40" width="897" height="40" fill="url(#bandGradient)"/>
      <rect x="0" y="32" width="560" height="4" fill="var(--green)"/>
      <rect x="560" y="32" width="337" height="4" fill="var(--yellow)"/>
    </svg>
  </div>
</body>
</html>
```